Etiketten für eine Apotherflasche
Zielgruppe
Wir sind eine Familienbrennerei aus Karlsruhe-Bulach, die von Vater und Tochter geführt wird. Wir stellen Edeldestillate, Whiskys, Gins und Liköre in Handarbeit her und legen großen Wert auf die Verwendung regionaler Rohstoffe, hauptsächlich von unseren eigenen Streuobstwiesen.
Aufgabenstellung
Wir benötigen ein Flaschenetikett für eine klassische Apotherflasche 0,5 Liter.
Der Inhalt wird unser 'Feldmarer Gin' sein.
Das Etikett sollte auf jeden Fall den Produktnamen 'Feldmarer Gin' enthalten.
Es wäre schön, wenn das Desgin die Stadt Karlsruhe wiederspiegeln würde - z.B. Fächer (da Fächerstadt), Stadtkarte im Hintergrund, Pyramide (Wahrzeichen von Karlsruhe) - hier dürfen Sie gerne kreativ werden.
Informationen zu uns bzw. unserer Brennerei finden Sie unter www.valdenhof-brennerei.de.
Bitte nicht an den dort existierenden Etiketten orientieren - diese werden akteuell umgestellt.
Maße des Etiketts sollten ca. 95x85mm sein.
Wir freuen uns auf die

```html
<!DOCTYPE html>
<html lang="de">
<head>
<meta charset="utf-8">
<title>Feldmarer Gin – Flaschenetikett</title>
<link rel="stylesheet" href="https://fonts.googleapis.com/css2?family=Barlow+Condensed:wght@300;400;500;600;700;800&family=Caveat:wght@400&display=swap">
<style>
  :root {
    --paper: #ffffff;
    --ink: #505050;
    --ink-dark: #222222;
    --gold: #c9a06a;
    --pen: #27307e;
    --map-light: #e4e4e4;
    --map-dark: #c9c9c9;
    --stage: #ececec;
  }
  * { margin: 0; padding: 0; box-sizing: border-box; }
  html, body { width: 1200px; height: 2182px; overflow: hidden; background: var(--stage); }
  body { font-family: "Barlow Condensed", sans-serif; color: var(--ink); }

  .label { position: absolute; left: 0; top: 0; width: 1200px; height: 1075px; background: var(--paper); overflow: hidden; }
  .label__art { position: absolute; left: 0; top: 0; }

  .abs { position: absolute; white-space: nowrap; }
  .tagline { font-weight: 300; color: var(--gold); font-size: 22px; letter-spacing: 2.5px; transform: translateX(-50%); }
  .seal { position: absolute; left: 529px; top: 48px; width: 140px; height: 140px; border-radius: 50%; border: 1.5px solid var(--gold); display: flex; align-items: center; justify-content: center; text-align: center; }
  .seal__name { font-weight: 400; color: var(--gold); font-size: 16px; letter-spacing: 1.5px; line-height: 1.2; }

  .product-city { left: 600px; top: 208px; transform: translateX(-50%); font-weight: 700; font-size: 86px; letter-spacing: 10px; color: var(--ink); line-height: 1; }
  .product-kind { left: 600px; top: 300px; transform: translateX(-50%); font-weight: 700; font-size: 268px; letter-spacing: 2px; color: var(--ink); line-height: 1; }
  .product-sub { left: 600px; top: 556px; transform: translateX(-50%); font-weight: 400; font-size: 21px; letter-spacing: 2.5px; color: var(--gold); }

  .band-title { left: 605px; top: 814px; transform: translateX(-50%); font-weight: 700; font-size: 26px; letter-spacing: 3.2px; color: var(--ink); }
  .field-label { font-size: 14px; font-weight: 500; letter-spacing: 1.5px; color: var(--ink-dark); }
  .handwritten { font-family: "Caveat", cursive; color: var(--pen); }
  .spec { font-weight: 700; font-size: 37px; color: var(--ink); }

  .origin { left: 163px; top: 851px; font-size: 14.5px; letter-spacing: 1.6px; line-height: 22.5px; color: var(--ink-dark); font-weight: 400; text-align: center; }
  .maker { left: 923px; top: 853px; font-size: 15px; line-height: 23px; color: var(--ink-dark); }
  .maker__name { font-weight: 700; font-size: 16px; }
</style>
</head>
<body>
  <section class="label" aria-label="Etikett Feldmarer Gin">
    <svg class="label__art" width="1200" height="1075" viewBox="0 0 1200 1075">
      <defs>
        <linearGradient id="mapTone" x1="0" y1="0" x2="1" y2="1">
          <stop offset="0" stop-color="var(--map-light)"/>
          <stop offset="1" stop-color="var(--map-dark)"/>
        </linearGradient>
      </defs>
      <g role="img" aria-label="Stadtkarte von Karlsruhe im Hintergrund">
        <polygon points="0,0 0,800 1200,800 1200,0 1177,0 594,738 0,30" fill="url(#mapTone)"/>
        <polygon points="0,980 1200,980 1200,1075 0,1075" fill="url(#mapTone)"/>
      </g>
      <polygon points="0,30 594,738 1177,0 1200,0 1200,0 0,0" fill="var(--paper)"/>
      <polyline points="0,30 594,738 1200,-30" fill="none" stroke="var(--gold)" stroke-width="3"/>
      <!-- header rules -->
      <line x1="139" y1="96" x2="512" y2="96" stroke="var(--gold)" stroke-width="1.2"/>
      <line x1="187" y1="151" x2="512" y2="151" stroke="var(--gold)" stroke-width="1.2"/>
      <line x1="698" y1="96" x2="1071" y2="96" stroke="var(--gold)" stroke-width="1.2"/>
      <line x1="698" y1="151" x2="1024" y2="151" stroke="var(--gold)" stroke-width="1.2"/>
      <!-- pyramid marks -->
      <polygon points="594,738 535,800 653,800" fill="var(--gold)"/>
      <polygon points="535,980 653,980 594,1046" fill="var(--gold)"/>
      <!-- info band -->
      <rect x="0" y="800" width="1200" height="180" fill="var(--paper)"/>
      <line x1="0" y1="800" x2="1200" y2="800" stroke="var(--gold)" stroke-width="3"/>
      <line x1="0" y1="980" x2="1200" y2="980" stroke="var(--gold)" stroke-width="3"/>
      <polygon points="535,980 653,980 594,1046" fill="var(--gold)"/>
      <!-- spec table -->
      <g stroke="var(--gold)" stroke-width="1.2">
        <line x1="321" y1="850" x2="888" y2="850"/>
        <line x1="321" y1="922" x2="888" y2="922"/>
        <line x1="703" y1="850" x2="703" y2="922"/>
        <line x1="558" y1="922" x2="558" y2="980"/>
        <line x1="730" y1="922" x2="730" y2="980"/>
      </g>
      <!-- still icon area -->
      <rect x="102" y="852" width="48" height="62" rx="6" fill="var(--gold)" opacity="0.8" role="img" aria-label="Illustration einer Brennblase"/>
    </svg>

    <div class="abs tagline" style="left:391px; top:112px;">VALDENHOFS SELECTION</div>
    <div class="abs tagline" style="left:817px; top:111px;">HANDCRAFTED QUALITY</div>
    <div class="seal"><span class="seal__name">VALDENHOF<br>DISTILLERY</span></div>

    <h1 class="abs product-city">FELDMARER</h1>
    <div class="abs product-kind">GIN</div>
    <div class="abs product-sub">FAMILY DISTILLERY</div>

    <div class="abs band-title">ABGEFÜLLT UND DESTILLIERT IN KARLSRUHE</div>

    <div class="abs origin">WHISKY, GIN UND<br>EDELDESTILLATE<br>AUS KARLSRUHE</div>

    <div class="abs field-label" style="left:340px; top:855px;">BATCH</div>
    <div class="abs handwritten" style="left:414px; top:846px; font-size:62px;">08.02.2023</div>
    <div class="abs field-label" style="left:727px; top:855px;">BOTTLE</div>
    <div class="abs handwritten" style="left:800px; top:846px; font-size:62px;">04</div>

    <div class="abs field-label" style="left:340px; top:929px;">DISTILLER</div>
    <div class="abs handwritten" style="left:398px; top:922px; font-size:48px;">Valdenhof</div>
    <div class="abs spec" style="left:590px; top:930px;">48 VOL%</div>
    <div class="abs spec" style="left:753px; top:930px;">500ML</div>

    <div class="abs maker">
      <div class="maker__name">VALDENHOF BRENNEREI GMBH</div>
      <div>AHORNSTR. 18, 76135 KARLSRUHE</div>
      <div>WWW.VALDENHOF-BRENNEREI.DE</div>
    </div>
  </section>
</body>
</html>
```